FernLoop.com Redesign of website

In general, I'm looking for something less cluttered, simpler and cleaner than the existing design. New design does not need to look anything like current website. I will attach the new logo design to be incorporated into the new web design. As with the new logo, I’d like it to be playful, fun and have some "attitude”.

-BACKGROUND -
FernLoop connects people with local small businesses. The idea is to attract customers with sweepstakes and other game elements and through "coupon" discounts at their local retailers.
For the retailers, we'll offer targeted ads by ZIP code and lead generation on the back-end.

FernLoop.com needs some serious design overhaul in order to more clearly convey this message to business owners and customers alike. It also needs in improved aesthetic appeal.

-HOME PAGE CONTENT-
• Text: “Search for Hidden Marbles worth up to $1,000!”
• Text: “FernLoop is a game that uses the serial numbers on dollar bills. It’s a virtual scavenger hunt that rewards you with cash, prizes and discounts at local businesses.”
• Placeholder for demo video and area for dynamic text & other content
• All or part of the new logo design and/or “Z icon”
• Large input field where people enter serial numbers.
• “Top Players” section for the top 10 ranked players in the game
• Room for dynamic top & bottom menus. Eg: http://fernloop.com/members.php

- GENERAL MESSAGING -
What’s FernLoop/WTF? (What’s This For?)
PUBLIC: “FernLoop is a game that uses the serial numbers on dollar bills. It’s a virtual scavenger hunt that rewards you with cash, prizes and discounts at local businesses.
MERCHANTS: “It's a way to attract new customers by turning ordinary dollar bills into ‘circulating coupons’. We're calling it the un-coupon because there's no paper wasted in printing, no clipping and your ad gets viewed over and over again as it goes through circulation. “

How does it work?

Say you have a coffee shop and you'd like to attract some new faces to your store. Using your FernLoop account, you create an offer like "Get $2 off any drink when you pay with a FernLoop". This effectively doubles the value of your customer's dollar- and unlike a coupon; it allows you to reach out to this customer again, because customers are registered in our database with contact info.

Next decide how many FernLoops you'd like to create and then register those serial numbers for this offer.

Then put your FernLoops "into play" by spending them, using them as change from the till or handing them out as your "business card"... be creative!

On the FernLoop home page, gamers play for a chance to win prizes and cash rewards up to $1000 by entering serial numbers from dollar bills. Players in your ZIP code will always see you listed, but if they also happen to enter one of your FernLoops, your full ad will come up in the TOP position.

When a customer clicks "redeem" for your offer, you'll be notified and your business will be added to their favorites list so that you can let them know about other offers in the future.

And the best part is that as a Premier FernLoop Merchant, you'll get the exclusive listing for your business category!"

-EXAMPLES-
*Attached page designs are ideas only, not necessarily the format required. Logo design & Icon are required in whole or at least in part. Be creative. I want to generate excitement & encourage people to play, make it simple and easy to understand.

New Logo design

Online:
One example I keep coming back to is the attitude of Tandrowe.com. Here are some other links from sites that I like the design and/or color scheme of:

www.slatenook.com
http://www.pellavine.com/seattle/
http://www.quorvanhub.com/
http://www.motrelly.com/?redirect_p=0
http://travela.tandrowe.com/rewards/
http://travela.tandrowe.com/promo/hotelBidAlerts.do

I'm attaching a couple more files just to give ideas. One is a sky/grass scene. Could something like that work as the primary background? Play with this idea if you like it, not necessary though. It may be something for other pages...

Also attaching samples of leader boards that I liked the format of. Would like the top ranked players to have these columns: 1. Ranking number (1 at top), 2. player name, City 3. FernLoop Score (or FL Score?) 4. small image space for icon/badge. Also open to your creative ideas on this...
Updates

I'm seeing some good designs- thank you!  Just a quick update because I've seen this a few times; if using images of paper money in the design, please don't include any denominations besides one dollar bills because we won't be using any other types of bills.  I don't want to give customers the wrong impression.  Thanks,

Hector

Hey designers, lots of good ideas coming in- keep it up! 

Quick update- I think I mentioned earlier, but please try to stick with images using one-dollar bills, (if using money images) not any other denominations like 10s or 50s because the website will only be using serial numbers from 1s and I don't want customers to get confused.

Another important point is that the entire purpose of the home page is to get people to enter serial numbers from dollar bills.  There will be other options and links on home page, but this one thing is the most important.  I just want them to get involved with the free contest and get more involved as they learn more about FernLoop, but no pressure to actually join  right away until they are more comfortable (membership will also be free).

Thank you!

Reason: I'll have more time to review through Monday the 12th, and want to be as thorough as possible. Thanks for all the great creative ideas! Hector

Target Market(s)

25 to 45 year-old men and women, internet savvy, gamers, environmentally-conscious,

Industry/Entity Type

Coffee Shop

Requirements
Must have
• -HOME PAGE CONTENT-
Nice to have
• ADDED: I'm uploading a couple of .pdf images of dollar bills fanned out that might look good incorporated into design. They may need a little touch-up to look smoothed out, if it's possible to remove the wrinkles.

Top Players leader board oriented vertically, as a column if it can be made to fit without making your page design too cluttered. Adding more images JUST FOR FUN, not required; adding some images for inspiration- eg the green brelmotor bug would be fun with FernLoop logo painted on side, looking like it's on the road, searching for bucks, green city sunrise bg might go along well with logo design...

```html
<!DOCTYPE html>
<html lang="en">
<head>
<meta charset="utf-8">
<title>FernLoop – Play. Discover. Support</title>
<link rel="stylesheet" href="https://fonts.googleapis.com/css2?family=Ribeye&family=Open+Sans:wght@400;600;700&family=Arimo:wght@400;700&display=swap">
<style>
  :root{
    --orange:#f58a0b;
    --green-dark:#0d5a12;
    --green:#149a1c;
    --green-bright:#2fb52c;
    --lime:#8fc31f;
    --cream:#fdf6df;
    --cream-2:#f6ecc6;
    --gold:#fcc93a;
    --gold-light:#fde7a0;
    --gold-deep:#e9a716;
    --text-dark:#3b2a0a;
    --red:#e0410f;
    --white:#ffffff;
  }
  *{box-sizing:border-box;margin:0;padding:0}
  html,body{width:1024px;height:1200px;overflow:hidden}
  body{position:relative;background:var(--cream);font-family:"Open Sans",Arial,sans-serif;color:var(--text-dark)}

  .site-header{position:absolute;left:0;top:0;width:1024px;height:123px;
    background:linear-gradient(#fff 0%,#fff 55%,var(--cream-2) 100%);border-top:4px solid var(--orange)}
  .brand{position:absolute;left:120px;top:26px;display:flex;align-items:center;gap:10px}
  .brand-mark{width:36px;height:36px;border-radius:50%;background:var(--green)}
  .brand-name{font-family:"Ribeye",serif;font-size:38px;color:var(--green);line-height:1}
  .brand-tagline{position:absolute;left:212px;top:82px;font-family:"Arimo",sans-serif;font-size:10.5px;font-weight:700;color:var(--green-dark)}
  .social{position:absolute;top:77px;left:785px;display:flex;gap:13px}
  .social a{display:block;width:31px;height:31px;border-radius:5px}
  .social .s1{background:#2f5ea8}.social .s2{background:#5ec3ea}.social .s3{background:#1c7cb4}

  .main-nav{position:absolute;left:0;top:123px;width:1024px;height:29px;
    background:linear-gradient(var(--green-bright),var(--green));display:flex;padding-left:120px;align-items:stretch}
  .main-nav a{font-family:"Arimo",sans-serif;font-weight:700;font-size:11.5px;color:var(--white);text-decoration:none;
    display:flex;align-items:center;padding:0 15.5px;border-right:1px solid rgba(0,0,0,.25)}
  .main-nav a:last-child{border-right:0}
  .main-nav a.is-active{background:var(--orange);padding:0 16px;border-right:0}

  .hero{position:absolute;left:0;top:152px;width:1024px;height:362px;overflow:hidden;
    background:linear-gradient(115deg,#0a3d0d 0%,#1c6b1e 35%,#0d4b10 60%,#166a19 80%,#08380b 100%)}
  .hero-visual{position:absolute;left:128px;top:30px;width:555px;height:290px;
    background:radial-gradient(ellipse at 55% 45%,rgba(236,238,220,.55) 0%,rgba(200,210,180,.35) 55%,rgba(160,180,140,.12) 100%);
    border-radius:18px;transform:rotate(6deg);filter:blur(1px)}
  .hero-arrow{position:absolute;left:530px;top:100px}
  .hero-title{position:absolute;right:136px;top:47px;text-align:right;font-family:"Ribeye",serif;font-weight:400;font-size:16.5px;color:var(--white);line-height:23px;letter-spacing:.3px}
  .hero-title span{color:var(--gold);display:block}
  .serial-search{position:absolute;left:675px;top:233px;width:229px;height:35px;border-radius:6px;background:var(--cream);
    display:flex;align-items:center;justify-content:space-between;padding:0 10px}
  .serial-search span{font-family:"Arimo",sans-serif;font-size:11.5px;color:var(--green)}

  .content{position:absolute;left:0;top:514px;width:1024px;height:617px;
    background:linear-gradient(180deg,#fbefc6 0%,#fdf8e8 35%,#fcf4dc 100%)}
  .intro{position:absolute;left:122px;top:15px;width:528px;text-align:center;font-family:"Ribeye",serif;font-style:italic;
    font-size:21.5px;line-height:33.6px;color:var(--lime);letter-spacing:2.4px;word-spacing:3px}
  .video{position:absolute;left:675px;top:31px;width:229px;height:163px;border:4px solid var(--white);
    background:linear-gradient(#565656,#2d2d2d);box-shadow:0 0 3px rgba(0,0,0,.3)}
  .play-btn{position:absolute;left:61px;top:58px;width:106px;height:30px;border:2px solid var(--white);border-radius:16px;
    background:rgba(0,0,0,.35);color:var(--white);font-family:"Arimo",sans-serif;font-size:11px;display:flex;align-items:center;padding-left:11px;gap:9px}
  .play-btn i{width:20px;height:20px;border-radius:50%;background:var(--white);display:flex;align-items:center;justify-content:center}
  .divider{position:absolute;left:189px;top:206px;width:393px;height:2px;background:linear-gradient(90deg,transparent,var(--gold-deep),transparent)}

  .panel{position:absolute;top:231px;height:315px;background:linear-gradient(var(--gold),var(--gold-light))}
  .panel h2{font-family:"Ribeye",serif;font-weight:400;font-size:21px;color:var(--green-dark);text-align:center;margin-top:14px}
  .coupon{left:120px;width:482px}
  .coupon-body{position:absolute;left:9px;top:44px;width:458px;height:245px;border-radius:12px;background:var(--gold);
    text-align:center;padding:38px 2px 0;font-size:11px;font-weight:700;line-height:19.5px;letter-spacing:-.15px}
  .coupon-body .lead{color:var(--red);font-style:italic;line-height:16px;margin-bottom:20px}
  .coupon-body p+p{margin-top:19px}
  .mascot{position:absolute;left:590px;top:315px;width:52px;height:92px;border-radius:50%;
    background:radial-gradient(ellipse,rgba(180,230,195,.55),rgba(180,230,195,0) 70%)}

  .leaders{left:675px;width:229px}
  .leaders-body{position:absolute;left:11px;top:44px;width:210px;height:245px;border-radius:12px;background:var(--gold);padding:8px 9px}
  .leaders-head{display:flex;justify-content:space-between;font-size:12px;color:var(--green-dark);padding:0 6px 5px 8px}
  .leaders-row{display:flex;justify-content:space-between;height:20px;margin-bottom:1.6px;padding:0 6px;
    background:linear-gradient(#f3b52a,#e49d0d);font-size:11.5px;font-weight:700;align-items:center}
  .leaders-row .pts{color:var(--white);font-size:12px}

  .money-stack{position:absolute;left:120px;top:528px;width:128px;height:80px;border-radius:50%;
    background:radial-gradient(ellipse at 65% 45%,rgba(79,198,42,.55) 0%,rgba(200,220,180,.35) 50%,rgba(200,220,180,0) 75%)}
  .login-btn{position:absolute;left:677px;top:564px;width:227px;height:36px;border-radius:5px;text-decoration:none;
    background:linear-gradient(var(--gold),var(--orange));font-family:"Ribeye",serif;font-size:18px;color:var(--green-dark);
    display:flex;align-items:center;padding-left:18px;box-shadow:0 2px 2px rgba(0,0,0,.2)}
  .login-btn .dot{position:absolute;right:10px;top:-8px;width:50px;height:50px;border-radius:50%;background:radial-gradient(#7edc3a,#1c8b16);border:3px solid #2a2a2a}

  .site-footer{position:absolute;left:0;top:1131px;width:1024px;height:69px;background:linear-gradient(var(--green-bright),var(--green))}
  .footer-links{position:absolute;left:121px;top:17px;font-family:"Arimo",sans-serif;font-size:10px;color:var(--white)}
  .footer-links a{color:var(--white);text-decoration:none}
  .footer-links em{font-style:normal;margin:0 4px}
  .copyright{position:absolute;left:121px;top:38px;font-family:"Arimo",sans-serif;font-size:10px;color:var(--white)}
  .footer-brand{position:absolute;left:790px;top:18px;display:flex;align-items:center;gap:7px}
  .footer-brand .brand-mark{width:28px;height:28px;background:var(--white)}
  .footer-brand .brand-name{font-size:25px;color:var(--white)}
</style>
</head>
<body>
  <header class="site-header">
    <div class="brand"><span class="brand-mark"></span><span class="brand-name">FernLoop</span></div>
    <div class="brand-tagline">Play. Discover. Support</div>
    <nav class="social" aria-label="Social links">
      <a class="s1" href="#" aria-label="Social link"></a>
      <a class="s2" href="#" aria-label="Social link"></a>
      <a class="s3" href="#" aria-label="Social link"></a>
    </nav>
  </header>

  <nav class="main-nav">
    <a class="is-active" href="#">Home</a>
    <a href="#">WTF ?</a>
    <a href="#">Customers</a>
    <a href="#">Big Picture</a>
    <a href="#">Contact</a>
    <a href="#">Business Owners</a>
    <a href="#">FernBlog &amp; Gear</a>
    <a href="#">Member Log-in</a>
    <a href="#">Sign Up</a>
  </nav>

  <section class="hero">
    <div class="hero-visual" role="img" aria-label="Hand holding a one-dollar bill with a magnifying glass over its serial number"></div>
    <svg class="hero-arrow" width="260" height="140" viewBox="0 0 260 140" aria-hidden="true">
      <path d="M10 60 C80 20,200 10,245 120" fill="none" stroke="#f5a21b" stroke-width="3"/>
      <path d="M232 112 L246 128 L252 106" fill="none" stroke="#f5a21b" stroke-width="3"/>
    </svg>
    <h1 class="hero-title">Search for Hidden Marbles worth<span>Up to $1,000!</span></h1>
    <div class="serial-search">
      <span>Enter serial number</span>
      <svg width="24" height="24" viewBox="0 0 24 24" aria-hidden="true"><circle cx="10" cy="10" r="7" fill="none" stroke="#0d5a12" stroke-width="3"/><path d="M15 15 L22 22" stroke="#0d5a12" stroke-width="3.5" stroke-linecap="round"/></svg>
    </div>
  </section>

  <main class="content">
    <p class="intro">FernLoop is a game that uses the serial numbers on dollar bills. It's a virtual scavenger hunt that rewards you with cash, prizes and discounts at local businesses.</p>

    <div class="video">
      <div class="play-btn">Click to play <i><svg width="8" height="10" viewBox="0 0 8 10"><path d="M0 0 L8 5 L0 10Z" fill="#333"/></svg></i></div>
    </div>
    <div class="divider"></div>

    <section class="panel coupon">
      <h2>Your Dollar is Also A Coupon!</h2>
      <div class="coupon-body">
        <p class="lead">YOU CAN REDEAM "FERNLOOPS" FOR CASH,PRIZES<br>AND DEALS AT YOUR PARTICIPATING NEIGHBORHOOD BUSINESSES.</p>
        <p>We're calling it the un-coupon because there's no paper wasted in printing.and no cliping. your dollar is your coupon!</p>
        <p>Enter the serial number from ANY dollar to see if you've won! They could be any where-including in your wallet-right now. While you're checking your dollars,check out our local merchants where you can also usethose same bucks as " Coupons" to get discounts at any FernLoop merchant in your area.</p>
      </div>
    </section>
    <div class="mascot" role="img" aria-label="Mascot character in sunglasses"></div>

    <section class="panel leaders">
      <h2>Top Players</h2>
      <div class="leaders-body">
        <div class="leaders-head"><span>Name</span><span>Point</span></div>
        <div class="leaders-row"><span>Marlon Petrie</span><span class="pts">758</span></div>
        <div class="leaders-row"><span>Tessa Brandell</span><span class="pts">630</span></div>
        <div class="leaders-row"><span>Allie Schonberg</span><span class="pts">498</span></div>
        <div class="leaders-row"><span>Rowan Lachter</span><span class="pts">450</span></div>
        <div class="leaders-row"><span>Alina Cortley</span><span class="pts">398</span></div>
        <div class="leaders-row"><span>Kody Brennick</span><span class="pts">268</span></div>
        <div class="leaders-row"><span>Kelvin Durrow</span><span class="pts">250</span></div>
        <div class="leaders-row"><span>Sula Brede</span><span class="pts">203</span></div>
        <div class="leaders-row"><span>Lamont Jarvis</span><span class="pts">200</span></div>
        <div class="leaders-row"><span>Carmina Jetley</span><span class="pts">150</span></div>
      </div>
    </section>

    <div class="money-stack" role="img" aria-label="Stack of one-dollar bills beside a green coin"></div>
    <a class="login-btn" href="#">Member Login<span class="dot"></span></a>
  </main>

  <footer class="site-footer">
    <div class="footer-links">
      <a href="#">Customers</a><em>|</em><a href="#">Big Picture</a><em>|</em><a href="#">Contact</a><em>|</em><a href="#">Business Owners</a><em>|</em><a href="#">FL Gear</a><em>|</em><a href="#">Privacy Policy</a><em>|</em><a href="#">Terms and Conditions</a><em>|</em><a href="#">Contest Rules</a>
    </div>
    <div class="copyright">© 2013 FernLoop, LLC.. All rights reserved.</div>
    <div class="footer-brand"><span class="brand-mark"></span><span class="brand-name">FernLoop</span></div>
  </footer>
</body>
</html>
```